QuoteMarlin.com Homepage Redesign

Create a new homepage design for our website QuoteMarlin.com. Our current experience is focused on auto insurance only. We would like to incorporate the ability to receive rate estimates for home insurance and bundled (home + auto) insurance in addition to auto. Home insurance will include home, renters and condo. The final design should inspire users to utilize our comparison tool.

Industry/Entity Type

Insurance (Auto & Home)

Number of Pages Required

1 page

Font styles to use
Other font styles liked:
• See Assets - Sans Serif & Roboto

Colors
0054AA
0677BA
7BADD7
CADEEF
E8F1F8
59FF00
82FF00
B8FF75
E3FFCB
F4FFEA

Requirements
Must have
• Must include the ability to launch our rate comparison tool within the main hero image for Auto, Home, Bundled.
Nice to have
• The design should be bold and eye catching. It should be differentiated from the typical landing page experience. (Some of our favorite sites from a UX perspective include: Vaultline.org, ThePelican.com, Ferrow.com and Corvane Airways - They are busy but we like the app like approach on the homepage)
Should not have
• We are not looking for a design that is heavy on generic images.

```html
<!DOCTYPE html>
<html lang="en">
<head>
<meta charset="utf-8">
<title>Quote Marlin – Home &amp; Car Insurance Rate Estimates</title>
<link href="https://fonts.googleapis.com/css2?family=Roboto:wght@400;500;700&display=swap" rel="stylesheet">
<style>
:root{
  --blue:#0a5ff0;
  --navy:#0b1f4b;
  --text:#3a4766;
  --muted:#7d8aa5;
  --band:#e8f0f9;
  --line:#c6d3e6;
  --white:#ffffff;
  --row:#eaf1fa;
  --deco-a:#c9dafb;
  --deco-b:#7fa6f4;
}
*{box-sizing:border-box;margin:0;padding:0}
html,body{width:1200px;height:4351px;overflow:hidden}
body{position:relative;font-family:"Roboto",sans-serif;color:var(--navy);background:var(--white)}
.abs{position:absolute}
.accent{color:var(--blue)}
.btn{position:absolute;background:var(--blue);color:var(--white);border-radius:20px;font-size:13px;font-weight:500;display:flex;align-items:center;justify-content:center;box-shadow:0 4px 10px rgba(10,95,240,.3)}
.art{position:absolute;border-radius:12px}
.deco{position:absolute;background:linear-gradient(135deg,var(--deco-a),var(--deco-b));opacity:.55}

/* header */
.top-bg{position:absolute;left:0;top:0;width:1200px;height:700px;background:linear-gradient(180deg,#e6eef9 0%,#f4f7fc 60%,#fff 100%)}
.brand{position:absolute;left:106px;top:20px;display:flex;align-items:center;gap:10px;font-size:22px;font-weight:700;color:var(--navy)}
.brand i{width:22px;height:22px;background:var(--blue);border-radius:50%;display:block}
.nav{position:absolute;top:27px;left:580px;display:flex;gap:40px;font-size:12px;color:var(--navy)}
.nav-cta{left:988px;top:18px;width:106px;height:33px;font-size:12px}

/* hero */
.hero-card{position:absolute;left:189px;top:90px;width:820px;height:523px;background:rgba(255,255,255,.92);border-radius:30px;box-shadow:0 10px 40px rgba(40,80,150,.12)}
.hero-title{position:absolute;left:189px;width:820px;top:114px;text-align:center;font-size:30px;font-weight:500}
.hero-sub{position:absolute;left:189px;width:820px;top:158px;text-align:center;font-size:12px;color:var(--text)}
.field{position:absolute;left:272px;width:321px;height:40px;border:1px solid #b9c3d3;border-radius:6px;font-size:12px;color:var(--muted);padding:0 20px;display:flex;align-items:center;justify-content:space-between;background:#fff}
.field b{width:0;height:0;border-left:5px solid transparent;border-right:5px solid transparent;border-top:6px solid var(--navy)}
.radio-row{position:absolute;left:272px;font-size:12px;color:var(--muted);display:flex;gap:14px;align-items:center}
.radio-row span.o{display:inline-flex;align-items:center;gap:6px}
.radio-row span.o::before{content:"";width:8px;height:8px;border:2px solid var(--blue);border-radius:50%}
.tagline{position:absolute;left:189px;width:820px;top:572px;text-align:center;font-size:18px;font-weight:500}
.tagline em{font-style:normal;color:var(--blue);margin:0 10px}

/* features */
.band{position:absolute;left:0;width:1200px;background:var(--band)}
.h2{font-size:30px;font-weight:500;line-height:1.4}
.feat-icon{position:absolute;left:529px;width:30px;height:30px}
.feat-title{position:absolute;left:580px;font-size:13px;font-weight:500}
.feat-text{position:absolute;left:580px;width:520px;font-size:13px;line-height:27px;color:var(--text)}

/* steps */
.step{position:absolute;top:1595px;width:264px;height:203px;background:#fff;border-radius:14px;box-shadow:0 6px 24px rgba(40,80,150,.12);text-align:center}
.step .n{margin-top:32px;font-size:13px;font-weight:500;color:var(--blue);letter-spacing:1px}
.step .t{margin-top:22px;font-size:14px;font-weight:500}
.step .d{margin:18px auto 0;width:160px;font-size:12px;line-height:27px;color:var(--text)}

/* table */
.tbl-row{position:absolute;left:105px;width:985px;height:45px;font-size:12px;display:flex;align-items:center;padding-left:86px;color:var(--navy)}
.tbl-row.alt{background:var(--row)}
.hl-col{position:absolute;left:635px;top:2087px;width:154px;height:364px;border:2px solid var(--blue);border-radius:10px}
.mark{position:absolute;width:16px;height:16px}

/* faq */
.faq{position:absolute;left:189px;width:820px;background:#fff;box-shadow:0 4px 20px rgba(40,80,150,.12);border-radius:4px}
.faq .q{position:absolute;left:30px;font-size:14px;font-weight:500}
.faq .pm{position:absolute;right:30px;font-size:24px;color:var(--blue);line-height:1}
.faq-body{position:absolute;left:34px;top:68px;font-size:12px;line-height:27px;color:var(--text)}
.faq-body b{font-weight:500;color:var(--navy)}

/* footer */
.f-col{position:absolute;top:4085px;font-size:12.5px;color:var(--muted)}
.f-col h4{font-size:13px;font-weight:500;color:var(--navy);margin-bottom:18px}
.f-col p{height:34px}
</style>
</head>
<body>

<div class="top-bg"></div>
<div class="deco" role="img" aria-label="Decorative blue 3D ornament" style="left:0;top:220px;width:150px;height:240px"></div>
<div class="deco" role="img" aria-label="Decorative blue 3D ribbon" style="left:1010px;top:310px;width:190px;height:230px"></div>

<header>
  <div class="brand"><i></i>Quote Marlin</div>
  <nav class="nav"><span>Car Insurance</span><span>Life Insurance</span><span>Resources</span><span>Company</span></nav>
  <div class="btn nav-cta">Compare Now</div>
</header>

<section class="hero">
  <div class="hero-card"></div>
  <h1 class="hero-title">Get A Rate Estimates For <span class="accent">Home &amp; Car Insurance</span></h1>
  <p class="hero-sub">See What You Should Pay At Top Companies Near You</p>
  <div class="field" style="top:193px">Enter Zip Code</div>
  <div class="field" style="top:250px">Current Provider<b></b></div>
  <div class="field" style="top:306px">How Old Are You</div>
  <div class="field" style="top:362px">Credit Score<b></b></div>
  <div class="radio-row" style="top:430px">Do You Own Your Home?<span class="o" style="margin-left:12px">Yes</span><span class="o">No</span></div>
  <div class="radio-row" style="top:461px">Do You Bundle Your Insurance?<span class="o" style="margin-left:12px">Yes</span><span class="o">No</span></div>
  <div class="btn" style="left:272px;top:504px;width:321px;height:40px">See Result</div>
  <div class="art" role="img" aria-label="3D illustration of a small blue vintage car" style="left:625px;top:220px;width:355px;height:287px;background:linear-gradient(160deg,#dfe8f7,#5f92f3)"></div>
  <p class="tagline">Quick<em>•</em>Private<em>•</em>Reliable Results.</p>
</section>

<section>
  <div class="band" style="top:738px;height:606px"></div>
  <div class="art" role="img" aria-label="3D illustration of a confident woman in blue overalls" style="left:93px;top:794px;width:347px;height:550px;border-radius:12px 12px 0 0;background:linear-gradient(180deg,#f0d2bf 0%,#b3dcee 45%,#4f86d2 100%)"></div>
  <h2 class="h2 abs" style="left:526px;top:758px">Everything You Need To<br>Make The <span class="accent">Right Decisions</span></h2>

  <svg class="feat-icon" style="top:870px" viewBox="0 0 30 30" fill="none" stroke="#0a5ff0" stroke-width="2"><circle cx="15" cy="15" r="11"/><circle cx="15" cy="15" r="6"/><circle cx="15" cy="15" r="1.5" fill="#0a5ff0"/></svg>
  <div class="feat-title" style="top:870px">No Bait And Switch – Accurate Rate Estimates Using Better Data</div>
  <p class="feat-text" style="top:902px">No Low-Ball Quotes. We Use The Rating Plans Submitted By Each Insurance Carrier To The State Department Of Insurance Plus Any Applicable Discounts To More Accurately Calculate What You Can Expect To Pay.</p>

  <svg class="feat-icon" style="top:1010px" viewBox="0 0 30 30" fill="none" stroke="#0a5ff0" stroke-width="2"><rect x="3" y="3" width="10" height="10" rx="2"/><rect x="17" y="3" width="10" height="10" rx="2"/><rect x="3" y="17" width="10" height="10" rx="2"/><rect x="17" y="17" width="10" height="10" rx="2" transform="rotate(45 22 22)"/></svg>
  <div class="feat-title" style="top:1010px">More Choices – Not Limited To Paid Advertisers</div>
  <p class="feat-text" style="top:1041px">Unlike Other Sites, Our Results Are Not Limited To Paid Sponsors. Our Results Represent Top Carriers In Your Geographic Area Based On The Total Premiums Written.</p>

  <svg class="feat-icon" style="top:1147px" viewBox="0 0 30 30" fill="none" stroke="#0a5ff0" stroke-width="2.2"><circle cx="15" cy="15" r="12"/><line x1="7" y1="23" x2="23" y2="7"/></svg>
  <div class="feat-title" style="top:1145px">Spam-Free - No Contact Information Required</div>
  <p class="feat-text" style="top:1176px">We Are The Only Insurance Comparison Tool That Does Not Require Your Contact Information To Generate Your Estimates, So You Can Be Sure You Won't Get Spam From Us.</p>

  <div class="btn" style="left:580px;top:1281px;width:125px;height:34px">Compare Now</div>
</section>

<section>
  <div class="deco" role="img" aria-label="Decorative blue 3D ornament" style="left:17px;top:1437px;width:160px;height:160px"></div>
  <div class="deco" role="img" aria-label="Decorative blue 3D ornament" style="left:1014px;top:1437px;width:160px;height:160px"></div>
  <h2 class="h2 abs" style="left:0;width:1200px;top:1428px;text-align:center">Insurance Shopping Can Be Pleasant - Like A<br>Relaxing Scroll Through <span class="accent">The Best Rates</span></h2>
  <p class="abs" style="left:0;width:1200px;top:1541px;text-align:center;font-size:14px;font-weight:500">Start Saving In 3 Simple Steps</p>
  <div class="step" style="left:166px"><div class="n">STEP 1</div><div class="t">Quick Start</div><div class="d">Answer 5 Questions. No Phone Number Or Email Required.</div></div>
  <div class="step" style="left:467px"><div class="n">STEP 2</div><div class="t">Retrieve Your Rates</div><div class="d">We Estimate How Much You'll Pay At Each Top Provider In Your State.</div></div>
  <div class="step" style="left:768px"><div class="n">STEP 3</div><div class="t">Compare And Save</div><div class="d">Compare Apples To Apples Pricing To Find Your Next Provider.</div></div>
  <div class="btn" style="left:546px;top:1829px;width:106px;height:34px">Get Started</div>
</section>

<section>
  <h2 class="h2 abs" style="left:0;width:1200px;top:1948px;text-align:center">Your Free And Impartial Insurance <span class="accent">Research Tool</span></h2>
  <p class="abs" style="left:160px;width:880px;top:2010px;text-align:center;font-size:12px;line-height:27px;color:var(--text)">We're Passionate About Giving You Open Access To The Data You Need To Make Smart Insurance Decisions. We Don't Sell Insurance Policies Directly – Our Tool Allows You Independently Research Your Options And Seamlessly Connect With The Provider That Works For You.</p>
  <div class="abs" style="left:635px;width:154px;top:2105px;text-align:center;font-size:12px;font-weight:500">Quote Marlin</div>
  <div class="abs" style="left:880px;width:154px;top:2105px;text-align:center;font-size:12px;font-weight:500">Other Comparison Sites</div>

  <div class="tbl-row" style="top:2141px">Connects You With The Provider You Choose</div>
  <div class="tbl-row alt" style="top:2186px">No Email Or Phone Number Required</div>
  <div class="tbl-row" style="top:2231px">Rates For All Top Companies In Your State</div>
  <div class="tbl-row alt" style="top:2276px">Accurate Rates Verified With State-Approved Rating Plans</div>
  <div class="tbl-row" style="top:2321px">Results Not Limited To Companies With Paid Sponsorships</div>
  <div class="tbl-row alt" style="top:2366px">Results Shown After Just 5 Questions</div>
  <div class="tbl-row" style="top:2411px">Option To Purchase A Policy Through Them</div>
  <div class="hl-col"></div>

  <svg width="0" height="0" style="position:absolute">
    <defs>
      <symbol id="yes" viewBox="0 0 16 16"><circle cx="8" cy="8" r="8" fill="#0a5ff0"/><path d="M4.5 8.2l2.3 2.3 4.7-4.8" stroke="#fff" stroke-width="1.8" fill="none"/></symbol>
      <symbol id="no" viewBox="0 0 16 16"><circle cx="8" cy="8" r="7" fill="none" stroke="#9aa4b5"/><path d="M5.5 5.5l5 5M10.5 5.5l-5 5" stroke="#9aa4b5"/></symbol>
    </defs>
  </svg>
  <svg class="mark" style="left:704px;top:2155px"><use href="#yes"/></svg>
  <svg class="mark" style="left:704px;top:2200px"><use href="#yes"/></svg>
  <svg class="mark" style="left:704px;top:2245px"><use href="#yes"/></svg>
  <svg class="mark" style="left:704px;top:2290px"><use href="#yes"/></svg>
  <svg class="mark" style="left:704px;top:2335px"><use href="#yes"/></svg>
  <svg class="mark" style="left:704px;top:2380px"><use href="#yes"/></svg>
  <svg class="mark" style="left:704px;top:2425px"><use href="#no"/></svg>
  <svg class="mark" style="left:949px;top:2155px"><use href="#yes"/></svg>
  <svg class="mark" style="left:949px;top:2200px"><use href="#no"/></svg>
  <svg class="mark" style="left:949px;top:2245px"><use href="#no"/></svg>
  <svg class="mark" style="left:949px;top:2290px"><use href="#no"/></svg>
  <svg class="mark" style="left:949px;top:2335px"><use href="#no"/></svg>
  <svg class="mark" style="left:949px;top:2380px"><use href="#no"/></svg>
  <svg class="mark" style="left:949px;top:2425px"><use href="#yes"/></svg>
</section>

<section>
  <div class="band" style="top:2565px;height:406px"></div>
  <h2 class="h2 abs" style="left:105px;top:2612px">Lifting The Curtain On The<br><span class="accent">Insurance Industry</span></h2>
  <p class="abs" style="left:105px;width:545px;top:2708px;font-size:12px;line-height:27px;color:var(--text)">Insurance Companies Have Rating Plans That Detail How They Use Certain Characteristics To Assign Different Rates To Different People. These Rating Plans Must Be Approved By Your State Department Of Insurance But Are Not Typically Available To Consumers.</p>
  <p class="abs" style="left:105px;width:545px;top:2816px;font-size:12px;line-height:27px;color:var(--text)">Quote Marlin Uses The Data From Each Insurance Company's Rating Plan (Plus Any Applicable Discounts) To More Accurately Calculate What You Can Expect To Pay.</p>
  <div class="btn" style="left:105px;top:2887px;width:125px;height:36px">Start Comparing</div>
  <div class="art" role="img" aria-label="3D illustration of a pastel house with green roof and trees" style="left:684px;top:2620px;width:443px;height:312px;background:linear-gradient(180deg,#7fb3ad 0%,#ecd9d3 55%,#cfdbef 100%)"></div>
</section>

<section>
  <div class="deco" role="img" aria-label="Decorative blue 3D ribbon" style="left:0;top:3330px;width:200px;height:140px"></div>
  <div class="deco" role="img" aria-label="Decorative blue 3D ribbon" style="left:1000px;top:3230px;width:200px;height:150px"></div>
  <h2 class="h2 abs" style="left:0;width:1200px;top:3054px;text-align:center">Frequently Asked Questions</h2>
  <div class="faq" style="top:3135px;height:301px">
    <div class="q" style="top:20px">Q1. How Does The Insurance Company Determine My Rate?</div>
    <div class="pm" style="top:14px">—</div>
    <div class="abs" style="left:0;top:56px;width:820px;border-top:1px solid #e6ebf3"></div>
    <div class="faq-body">
      Car Insurance Companies Determine How Much They Charge You Based On Your Driver Profile.<br>
      Factors That Can Impact Your Rates Include:<br>
      &nbsp;&nbsp;1. <b>Demographics</b> - Your Age, Home Ownership, Credit Score, And More<br>
      &nbsp;&nbsp;2. <b>Your Driving History</b> - How Long You've Been Driving, Traffic Violations, And More<br>
      &nbsp;&nbsp;3. <b>Your Car</b> - Make, Model, And Year<br>
      &nbsp;&nbsp;4. <b>Where You Live</b> - State And Zip Code<br>
      &nbsp;&nbsp;5. How Much <b>Coverage</b> You Want<br>
      &nbsp;&nbsp;<span class="accent">Read More</span>
    </div>
  </div>
  <div class="faq" style="top:3442px;height:51px">
    <div class="q" style="top:17px">Q2. How Do I Switch My Car Insurance?</div>
    <div class="pm" style="top:12px">+</div>
  </div>
  <div class="faq" style="top:3503px;height:53px">
    <div class="q" style="top:18px">Q3. How Is Quote Marlin Different Than Other Insurance Websites?</div>
    <div class="pm" style="top:13px">+</div>
  </div>
  <div class="btn" style="left:551px;top:3586px;width:97px;height:34px;font-size:11px">See all FAQ</div>
</section>

<section>
  <div class="band" style="top:3745px;height:260px"></div>
  <div class="art" role="img" aria-label="Abstract blue 3D shape decoration" style="left:684px;top:3745px;width:450px;height:260px;border-radius:0;background:linear-gradient(135deg,#c9dafb,#7fa6f4)"></div>
  <h2 class="h2 abs" style="left:105px;top:3802px">Ready, Set, <span class="accent">Retrieve</span></h2>
  <p class="abs" style="left:105px;top:3860px;font-size:12px;color:var(--text)">Ready To Get Started? Dig Up The Best Insurance Providers In Seconds</p>
  <div class="abs" style="left:105px;top:3899px;width:355px;height:41px;background:#fff;border:1px solid #d5dde9;font-size:12px;color:var(--muted);display:flex;align-items:center;padding-left:20px">Enter Your Zip Code</div>
  <div class="abs" style="left:460px;top:3899px;width:133px;height:41px;background:var(--blue);color:#fff;font-size:13px;font-weight:500;display:flex;align-items:center;justify-content:center">Compare Now</div>
</section>

<footer>
  <div class="abs" style="left:106px;top:4110px;display:flex;align-items:center;gap:10px;font-size:26px;font-weight:700"><span style="width:26px;height:26px;background:var(--blue);border-radius:50%;display:block"></span>Quote Marlin</div>
  <p class="abs" style="left:106px;top:4188px;width:330px;font-size:12.5px;line-height:27px;color:var(--muted)">Quote Marlin Is Your Insurance Companion – Connecting You With Top Auto Insurance Providers Without Collecting Your Contact Information.</p>
  <div class="f-col" style="left:522px"><h4>Resources</h4><p>FAQ</p><p>Insurance By State</p><p>Insurance By Age</p><p>See All</p></div>
  <div class="f-col" style="left:712px"><h4>Company</h4><p>Contact Us</p><p>How We Make Money</p><p>Spam-Free Promise</p><p>Partner With Us</p></div>
  <div class="f-col" style="left:936px"><h4>Support</h4><p>Editorial Policy</p><p>Accessibility Statement</p><p>Cookie Policy</p><p>California Residents: Do</p><p>Not Sell My Info</p></div>
  <div class="abs" style="left:105px;top:4306px;width:985px;border-top:1px solid var(--line)"></div>
  <p class="abs" style="left:0;width:1200px;top:4326px;text-align:center;font-size:11px;color:var(--text)">Copyright © Quote Marlin Insurance Services 2023. A Brightvane Company. All Rights Reserved.</p>
</footer>

</body>
</html>
```